Shopify Design for wedding invitations

We are a greeting card manufactory, special in wedding invitation
I need a shopify website for our wedding invitation brand. (Lovonna), atttach you can find our logo.
We are looking for someone to create a modern and clean looking e-commerce store for our wedding invitation through Shopify. We need some life, professionalism and style put into our site. We will have a variety serie of products : laser cut wedding invitation, popup wedding invitaiton, vintage wedding invitation, handmade wedding invitation, printing invitation, Custom wedding cards, wedding stationery (including favor box, table card, place card, escort card, number card), Thank you card. our online store requires easy navigation to categories divided by product type.

our market is , Eourpe and USA,
please choose a good color for it.
you can go to our website: www.bluepinecrafts.com and check our product.
also you can go to Shopvane 4 new items.
https://www.shopvane.com/dp/K47T8M2Q61?ref=myi_title_dp

Designs look the same

Target Market(s)

Europe and USA

Industry/Entity Type

wedding

Number of Pages Required

1 page

Requirements
Must have
• Logo, 3 banners than can be changed each 3-5 seconds.
Nice to have
• nice icon and font, beautiful color,

```html
<!DOCTYPE html>
<html lang="en">
<head>
<meta charset="utf-8">
<title>Lovonna — Wedding Invitations</title>
<link rel="stylesheet" href="https://fonts.googleapis.com/css2?family=Lato:wght@400;700&family=Sofia&display=swap">
<style>
:root{
  --green:#6f9a30;
  --green-dark:#5f8727;
  --nav:#1e1e1e;
  --text:#555;
  --white:#fff;
  --wood1:#7a3f1f;
  --wood2:#4a2310;
}
*{margin:0;padding:0;box-sizing:border-box}
html,body{width:1200px;height:2883px;overflow:hidden;background:var(--white)}
body{position:relative;font-family:'Lato',sans-serif;color:var(--text)}
.abs{position:absolute}
.script{font-family:'Sofia',cursive}

.topbar{top:0;left:0;width:1200px;height:27px;background:var(--white)}
.topbar .account{right:150px;top:5px;font-size:13px;font-weight:700;color:#222}
.topbar svg{right:120px;top:3px}

.mainnav{top:27px;left:0;width:1200px;height:75px;background:var(--nav)}
.logo{left:125px;top:12px;font-size:38px;color:var(--white)}
.menu{left:369px;top:27px;display:flex;gap:24px;font-size:14px;font-weight:700;color:var(--white)}
.menu .active{color:var(--green);border-bottom:2px solid var(--green);padding-bottom:4px}
.search{left:915px;top:22px;width:163px;height:26px;border-radius:13px;background:var(--white);font-size:11px;color:#bbb;padding:6px 10px}
.search svg{position:absolute;right:9px;top:7px}

.hero{top:102px;left:0;width:1200px;height:381px;background:linear-gradient(110deg,#3a1c12 0%,#8a4a2a 30%,#c9875a 50%,#5a3a4a 70%,#b86a3a 100%)}
.hero h1{left:40px;top:80px;width:640px;font-size:64px;line-height:80px;color:var(--white);font-weight:400;text-shadow:0 0 3px #000;text-align:center;white-space:nowrap}
.hero p{left:40px;top:268px;width:600px;text-align:center;font-size:28px;line-height:40px;color:var(--white);text-shadow:0 0 3px #000}

.sidebar{left:1136px;top:347px;width:52px;background:var(--white);box-shadow:0 0 4px rgba(0,0,0,.25)}
.sidebar div{height:50px;border-bottom:1px solid #e5e5e5;text-align:center;font-size:8px;color:#333;padding-top:6px}
.sidebar i{display:block;width:16px;height:16px;border-radius:50%;margin:0 auto 3px}

.heading{left:0;width:1200px;text-align:center;color:var(--green);font-weight:400;white-space:nowrap}
.dots{left:123px;width:953px;border-top:3px dotted var(--green)}

.about{left:125px;top:617px;width:950px;font-size:19px;line-height:27px;color:#555}
.about p+p{margin-top:27px}

.product{width:186px;text-align:center}
.product .photo{width:186px;height:186px;border:2px solid var(--green);background:linear-gradient(135deg,var(--wood1),var(--wood2))}
.product b{display:block;font-size:12px;color:#666;margin-top:14px}
.product span{display:block;font-size:12px;color:#777;margin-top:1px}
.product em{display:block;font-style:normal;font-weight:700;font-size:12px;color:var(--green);margin-top:6px}

.avatar{width:100px;height:100px;border-radius:50%;border:3px solid var(--green)}
.person{text-align:center;font-size:19px;line-height:27px;color:#555}
.person h3{font-size:32px;line-height:36px;color:var(--green);font-weight:700;margin-bottom:-4px}
.chip{width:36px;height:36px;border-radius:50%}

.field{left:123px;width:950px;border:3px dotted var(--green);border-radius:14px;font-size:28px;color:#777;padding:12px 8px}
.send{left:123px;top:2456px;width:196px;height:47px;border:3px dotted var(--white);outline:2px solid var(--green);background:var(--green);border-radius:10px;color:var(--white);font-weight:700;font-size:20px;text-align:center;line-height:41px}

.footer{left:0;top:2562px;width:1200px;height:321px;background:var(--green);color:var(--white)}
.social{top:50px;width:26px;height:26px;border-radius:50%;border:2px solid var(--white)}
.fcol{top:92px;font-size:13px;line-height:16px}
.fcol h4{font-size:16px;font-weight:700;margin-bottom:18px}
.fcol svg{position:absolute;left:-28px;top:40px}
.flinks{top:258px;left:0;width:1200px;text-align:center;font-size:14px;font-weight:700;word-spacing:2px}
.flinks span{margin:0 10px}
.copy{top:294px;left:0;width:1200px;text-align:center;font-size:13px;font-weight:700}
</style>
</head>
<body>

<header>
  <div class="abs topbar">
    <div class="abs account">Register &nbsp;&nbsp;/&nbsp;&nbsp; Login</div>
    <svg class="abs" width="24" height="22" viewBox="0 0 24 22"><path d="M1 2h4l3 12h12l2-8H7" fill="none" stroke="#222" stroke-width="2"/><circle cx="10" cy="18" r="2" fill="#222"/><circle cx="18" cy="18" r="2" fill="#222"/></svg>
  </div>
  <nav class="abs mainnav">
    <div class="abs logo script">Lovonna</div>
    <div class="abs menu">
      <span class="active">HOME</span><span>PRODUCTS</span><span>NEWS</span><span>ABOUT US</span><span>CONTACT US</span><span>SEND INQUIRY</span>
    </div>
    <div class="abs search">Please Enter Keyword
      <svg width="10" height="10" viewBox="0 0 10 10"><circle cx="4" cy="4" r="3" fill="none" stroke="#222" stroke-width="1.5"/><path d="M6 6l3 3" stroke="#222" stroke-width="1.5"/></svg>
    </div>
  </nav>
</header>

<section class="abs hero" role="img" aria-label="Photo of a smiling couple on a Venice canal gondola">
  <h1 class="abs script">Happy<br>Wedding Season</h1>
  <p class="abs script">Pass you's happiness and joy in in the<br>important days of your life</p>
</section>

<aside class="abs sidebar">
  <div><i style="background:#1a73e8"></i>Customer Service</div>
  <div><i style="background:#2ecc40"></i>Live Chat</div>
  <div><i style="background:#1ea0e0"></i>Voice Call</div>
  <div><i style="background:#3bbf3b"></i>Messenger</div>
  <div><i style="background:#f08a24"></i>Share</div>
  <div><i style="background:#2563eb;border-radius:3px"></i>Message</div>
  <div style="border:0"><svg width="16" height="16" viewBox="0 0 16 16" style="display:block;margin:0 auto 3px"><path d="M2 2h12M8 14V5M4 9l4-4 4 4" fill="none" stroke="#333" stroke-width="1.5"/></svg>Top</div>
</aside>

<main>
  <h2 class="abs heading script" style="top:522px;font-size:48px">Hangzhou Blue Pine Crafts Co., Ltd.</h2>
  <div class="abs dots" style="top:597px"></div>
  <div class="abs about">
    <p>Our company is established in 2001, located in Linhai, Zhejiang Province.We are an professional manufacturer and exporter that is concerned with the design, development and production manufacturing wedding invitation card, favor boxes and other gift items.</p>
    <p>Our company products all passed the CE, FSC and BSCI accreditation. We are able to provide high-quality products to customers from around the world, main market areas include Europe(Germany, UK, France, Italy), USA, Asian(Japan, Korea, India), South America. We have always been the most trusted partner of our customers.</p>
  </div>

  <h2 class="abs heading script" style="top:858px;font-size:48px">New Products</h2>
  <div class="abs dots" style="top:925px"></div>

  <div class="abs product" style="left:227px;top:953px"><div class="photo" role="img" aria-label="Burgundy laser-cut invitation with kraft envelope on wood"></div><b>PRODUCT 1</b><span>Vintage wedding invitation</span><em>US $ 0,81 - US $ 1.17</em></div>
  <div class="abs product" style="left:416px;top:953px"><div class="photo" role="img" aria-label="Gold butterfly laser-cut invitation on wood"></div><b>PRODUCT 2</b><span>Vintage wedding invitation</span><em>US $ 0,81 - US $ 1.17</em></div>
  <div class="abs product" style="left:606px;top:953px"><div class="photo" role="img" aria-label="Navy lace laser-cut invitation on wood"></div><b>PRODUCT 3</b><span>Vintage wedding invitation</span><em>US $ 0,81 - US $ 1.17</em></div>
  <div class="abs product" style="left:796px;top:953px"><div class="photo" role="img" aria-label="Gold glitter lace invitation on wood"></div><b>PRODUCT 4</b><span>Vintage wedding invitation</span><em>US $ 0,81 - US $ 1.17</em></div>
  <div class="abs product" style="left:227px;top:1232px"><div class="photo" role="img" aria-label="Burgundy laser-cut invitation with kraft envelope on wood"></div><b>PRODUCT 5</b><span>Vintage wedding invitation</span><em>US $ 0,81 - US $ 1.17</em></div>
  <div class="abs product" style="left:416px;top:1232px"><div class="photo" role="img" aria-label="Gold butterfly laser-cut invitation on wood"></div><b>PRODUCT 6</b><span>Vintage wedding invitation</span><em>US $ 0,81 - US $ 1.17</em></div>
  <div class="abs product" style="left:606px;top:1232px"><div class="photo" role="img" aria-label="Navy lace laser-cut invitation on wood"></div><b>PRODUCT 7</b><span>Vintage wedding invitation</span><em>US $ 0,81 - US $ 1.17</em></div>
  <div class="abs product" style="left:796px;top:1232px"><div class="photo" role="img" aria-label="Gold glitter lace invitation on wood"></div><b>PRODUCT 8</b><span>Vintage wedding invitation</span><em>US $ 0,81 - US $ 1.17</em></div>

  <h2 class="abs heading script" style="top:1520px;font-size:48px">Contact Us</h2>
  <div class="abs dots" style="top:1589px;left:121px"></div>

  <div class="abs avatar" style="left:126px;top:1636px;background:linear-gradient(135deg,#8a5a3a,#d8c0a0)" role="img" aria-label="Portrait photo of Daniel"></div>
  <div class="abs person" style="left:213px;width:360px;top:1617px"><h3>Daniel</h3>E-mail: admin@bluepinecrafts.com<br>Mobile phone: +86 13700482215<br>TEL: +86 13700482215</div>

  <div class="abs avatar" style="left:671px;top:1636px;background:linear-gradient(135deg,#6a7a5a,#c8c0b0)" role="img" aria-label="Portrait photo of Mira"></div>
  <div class="abs person" style="left:770px;width:320px;top:1619px"><h3>Mira</h3>E-mail: mira@bluepinecrafts.com<br>TEL: +86 18306417729</div>

  <div class="abs avatar" style="left:126px;top:1787px;background:linear-gradient(135deg,#2e5a7a,#d0d8e0)" role="img" aria-label="Portrait photo of Lena"></div>
  <div class="abs person" style="left:233px;width:320px;top:1769px"><h3>Lena</h3>E-mail: lena@bluepinecrafts.com<br>TEL: +86 18611730564</div>
  <div class="abs chip" style="left:343px;top:1872px;background:#2ecc40"></div>
  <div class="abs chip" style="left:407px;top:1872px;background:#1ea0e0"></div>

  <div class="abs avatar" style="left:671px;top:1787px;background:linear-gradient(135deg,#7aa0c0,#a08a7a)" role="img" aria-label="Portrait photo of Vera"></div>
  <div class="abs person" style="left:770px;width:320px;top:1769px"><h3>Vera</h3>E-mail: vera@bluepinecrafts.com<br>Mobile phone: +86 05763398410<br>TEL: +86 18822906473</div>
  <div class="abs chip" style="left:894px;top:1903px;background:#2ecc40"></div>
  <div class="abs chip" style="left:957px;top:1903px;background:#1ea0e0"></div>

  <div class="abs avatar" style="left:126px;top:1934px;background:linear-gradient(135deg,#4a4a5a,#c0a898)" role="img" aria-label="Portrait photo of Alma"></div>
  <div class="abs person" style="left:236px;width:300px;top:1929px"><h3>Alma</h3>E-mail: alma@blue-pine.com<br>TEL: +86 18306417729</div>

  <h2 class="abs heading script" style="top:2072px;font-size:48px">Send Message</h2>
  <div class="abs field" style="top:2156px;height:65px">*Email</div>
  <div class="abs field" style="top:2257px;height:171px">*Message Content</div>
  <div class="abs send">SEND MESSAGE</div>
</main>

<footer class="abs footer">
  <svg class="abs" style="left:0;top:-10px" width="1200" height="20" viewBox="0 0 1200 20">
    <g fill="#fff">
      <circle cx="5" cy="10" r="10"/><circle cx="55" cy="10" r="10"/><circle cx="105" cy="10" r="10"/><circle cx="155" cy="10" r="10"/><circle cx="205" cy="10" r="10"/><circle cx="255" cy="10" r="10"/><circle cx="305" cy="10" r="10"/><circle cx="355" cy="10" r="10"/><circle cx="405" cy="10" r="10"/><circle cx="455" cy="10" r="10"/><circle cx="505" cy="10" r="10"/><circle cx="555" cy="10" r="10"/><circle cx="605" cy="10" r="10"/><circle cx="655" cy="10" r="10"/><circle cx="705" cy="10" r="10"/><circle cx="755" cy="10" r="10"/><circle cx="805" cy="10" r="10"/><circle cx="855" cy="10" r="10"/><circle cx="905" cy="10" r="10"/><circle cx="955" cy="10" r="10"/><circle cx="1005" cy="10" r="10"/><circle cx="1055" cy="10" r="10"/><circle cx="1105" cy="10" r="10"/><circle cx="1155" cy="10" r="10"/><circle cx="1205" cy="10" r="10"/>
    </g>
  </svg>
  <div class="abs social" style="left:125px"></div>
  <div class="abs social" style="left:165px"></div>
  <div class="abs social" style="left:205px"></div>

  <div class="abs fcol" style="left:153px">
    <h4>Address</h4>
    <svg width="18" height="24" viewBox="0 0 18 24"><path d="M9 22s7-8 7-13a7 7 0 0 0-14 0c0 5 7 13 7 13z" fill="none" stroke="#fff" stroke-width="2"/><circle cx="9" cy="9" r="2.5" fill="none" stroke="#fff" stroke-width="2"/></svg>
    Rm B112, 3rd Floor,<br>Songlin Building,<br>Qiaohe Road, Linhai,<br>P.R. CHINA, 317000
  </div>
  <div class="abs fcol" style="left:403px">
    <h4>Telephone</h4>
    <svg width="22" height="22" viewBox="0 0 22 22"><path d="M4 2l4 1 2 5-3 2a12 12 0 0 0 5 5l2-3 5 2 1 4-3 2C10 20 2 12 2 5z" fill="none" stroke="#fff" stroke-width="1.8"/></svg>
    +86 13700482215<br>+86 18822906473<br>+86 18611730564<br>18306417729<br>+86 18306417729
  </div>
  <div class="abs fcol" style="left:659px">
    <h4>Mobile phone</h4>
    <svg width="16" height="24" viewBox="0 0 16 24"><rect x="1" y="1" width="14" height="22" rx="2" fill="none" stroke="#fff" stroke-width="2"/><path d="M6 19h4" stroke="#fff" stroke-width="2"/></svg>
    +86 13700482215<br>+86 05763398410
  </div>
  <div class="abs fcol" style="left:913px">
    <h4>E-mail</h4>
    <svg width="24" height="18" viewBox="0 0 24 18"><rect x="1" y="1" width="22" height="16" rx="2" fill="none" stroke="#fff" stroke-width="2"/><path d="M1 2l11 8 11-8" fill="none" stroke="#fff" stroke-width="2"/></svg>
    admin@bluepinecrafts.com<br>mira@bluepinecrafts.com<br>lena@bluepinecrafts.com<br>vera@bluepinecrafts.com<br>alma@blue-pine.com
  </div>

  <div class="abs flinks"><span>HOME</span><span>PRODUCTS</span><span>NEWS</span><span>ABOUT US</span><span>CONTACT US</span><span>SEND INQUIRY</span><span>SITEMAP</span></div>
  <div class="abs copy">2022 Hangzhou Blue Pine Crafts Co., ltd. (408117) All rights reserved</div>
</footer>

</body>
</html>
```